Modern Billboard Ad for Criminal Defense Firm

10.5 x 36 We're looking for something to set us apart from the local competition. Looking for sleek and modern. We're a mid-sized firm in a small market city. We want to give the artist room to be creative on this one.
Thanks

Target Market(s)

Adult clients who have been charged with a crime/DWI

Industry/Entity Type

legal

Font styles to use
Serif
Sans Serif

Requirements
Must have
• Needs to have the firm name in large lettering. Law Offices of Martin G Ashby. “PLLC” does not have to be included. Phone number of (555) 318-4092 should be included but not the main focus.
Nice to have
• A call to action or something similar. “Don’t go it alone, call today.”, “ Arrested?”

```html
<!DOCTYPE html>
<html lang="en">
<head>
<meta charset="utf-8">
<title>Law Offices of Martin G Ashby – Billboard</title>
<link rel="stylesheet" href="https://fonts.googleapis.com/css2?family=Bebas+Neue&family=Cinzel:wght@400;500&family=Tinos&display=swap">
<style>
  :root {
    --page-bg: #e6e9ed;
    --panel-light: #0a78a8;
    --panel-mid: #073a6b;
    --panel-dark: #041538;
    --ink-white: #ffffff;
    --accent-yellow: #ffe100;
    --rule: rgba(255, 255, 255, 0.7);
    --photo-top: #3d5a78;
    --photo-bottom: #1b2c42;
    --portrait-top: #7a6a5a;
    --portrait-bottom: #5d6570;
    --badge-blue: #27a3e0;
    --badge-dark: #1c1c22;
  }
  * { box-sizing: border-box; margin: 0; padding: 0; }
  html, body {
    width: 1200px;
    height: 1200px;
    overflow: hidden;
    background: var(--page-bg);
  }
  .canvas {
    position: relative;
    width: 1200px;
    height: 1200px;
  }
  .billboard {
    position: absolute;
    left: 40px;
    top: 436px;
    width: 1120px;
    height: 327px;
    overflow: hidden;
    background: linear-gradient(100deg, var(--panel-light) 0%, var(--panel-mid) 45%, var(--panel-dark) 75%, var(--panel-dark) 100%);
    box-shadow: 0 10px 30px rgba(0, 0, 0, 0.25);
  }
  .suspect-photo {
    position: absolute;
    left: 12px;
    top: 16px;
    width: 172px;
    height: 311px;
    background: linear-gradient(180deg, var(--photo-top) 0%, var(--photo-bottom) 100%);
    border-radius: 70px 70px 0 0;
  }
  .headline {
    position: absolute;
    left: 222px;
    top: 18px;
    font-family: "Bebas Neue", "Oswald", sans-serif;
    font-weight: 400;
    font-size: 92px;
    line-height: 1;
    letter-spacing: -0.5px;
    color: var(--ink-white);
    white-space: nowrap;
  }
  .headline .call-to-action { color: var(--accent-yellow); }
  .divider {
    position: absolute;
    left: 222px;
    top: 116px;
    width: 870px;
    height: 1px;
    background: var(--rule);
  }
  .firm-name {
    position: absolute;
    left: 222px;
    top: 128px;
    font-family: "Cinzel", "Trajan Pro", serif;
    font-weight: 400;
    font-size: 44px;
    line-height: 1;
    letter-spacing: 0.5px;
    text-transform: uppercase;
    color: var(--ink-white);
    white-space: nowrap;
  }
  .phone {
    position: absolute;
    left: 244px;
    top: 204px;
    display: flex;
    align-items: center;
    gap: 12px;
    font-family: "Tinos", "Times New Roman", serif;
    font-size: 78px;
    line-height: 1;
    color: var(--ink-white);
    white-space: nowrap;
  }
  .phone-icon { width: 48px; height: 53px; flex: none; }
  .attorney-portrait {
    position: absolute;
    left: 858px;
    top: 186px;
    width: 100px;
    height: 128px;
    border: 2px solid var(--ink-white);
    background: linear-gradient(180deg, var(--portrait-top) 0%, var(--portrait-bottom) 100%);
  }
  .award-badge {
    position: absolute;
    left: 976px;
    top: 176px;
    width: 102px;
    height: 136px;
    background: var(--badge-dark);
    border: 3px solid var(--badge-blue);
  }
  .award-badge::before {
    content: "";
    position: absolute;
    left: 0; right: 0; top: 0;
    height: 22px;
    background: var(--badge-blue);
  }
  .award-badge::after {
    content: "";
    position: absolute;
    left: 0; right: 0; bottom: 0;
    height: 22px;
    background: var(--badge-blue);
  }
</style>
</head>
<body>
  <main class="canvas">
    <section class="billboard">
      <div class="suspect-photo" role="img" aria-label="Photo of a hooded man in handcuffs holding out his hands"></div>

      <h1 class="headline">Don’t go it alone, <span class="call-to-action">call today.</span></h1>
      <div class="divider"></div>
      <h2 class="firm-name">Law Offices of Martin G. Ashby</h2>

      <p class="phone">
        <svg class="phone-icon" viewBox="0 0 40 44" aria-hidden="true">
          <path d="M9 4 L15 4 L17 14 L12 17 C14 24 17 29 22 33 L26 29 L35 33 L34 40 C20 41 5 27 4 10 Z" fill="#ffffff"/>
          <path d="M24 10 A8 8 0 0 1 30 17" stroke="#ffffff" stroke-width="2.5" fill="none" stroke-linecap="round"/>
          <path d="M25 4 A14 14 0 0 1 36 16" stroke="#ffffff" stroke-width="2.5" fill="none" stroke-linecap="round"/>
        </svg>
        <span class="phone-number">(555) 318-4092</span>
      </p>

      <div class="attorney-portrait" role="img" aria-label="Portrait photo of attorney Martin G. Ashby in a grey suit"></div>
      <div class="award-badge" role="img" aria-label="Community choice award badge"></div>
    </section>
  </main>
</body>
</html>
```